Quorra Desk Talk Chat Monitor Interface

We have a live help chat software that we need a new chat monitor interface designed for. Something that will be easy to make responsive. I will provide screen shots of the current interface and a picture of the new admin back-end that we want it to look similar too. This project should be fairly straight forward and easy. See below.

Important Notes:

1. You DO NOT need to worry about the actual list of visitors on the site in the middle as that will be handled by the grid system we use.

2. We have decided to eliminate the logo from the monitor all together to make it more compact. Just the words "Quorra Desk Talk" and a copyright notice will be enough.

3. We want the chat monitor interface to utilize the same colors and look as the new admin interface if possible. See attached "new_admin_interface.png" image.

4. Although I want to utilize the same colors as the admin area, it should NOT utilize the same header and footer as the admin area. I only referenced the admin area so that you can get color ideas from it. Consider it a popup window and assume the same amount of space will be used. Although it will have the ability to be resized we must not waste space.

Target Market(s)

N/A

Industry/Entity Type

Software

Number of Pages Required

1 page

Requirements
Must have
• See Description.
Nice to have
• See Description.
Should not have
• See Description.

```html
<!DOCTYPE html>
<html lang="en">
<head>
<meta charset="utf-8">
<title>Quorra Desk Talk Chat Monitor</title>
<link rel="stylesheet" href="https://fonts.googleapis.com/css2?family=Open+Sans:ital,wght@0,400;0,600;0,700;1,800&display=swap">
<style>
:root{
  --navy:#243447;
  --navy-text:#1f2d3d;
  --page:#e9e9e9;
  --panel:#ffffff;
  --grid-bg:#eff2f7;
  --line:#d3d6da;
  --head-top:#fbfbfb;
  --head-bottom:#e4e4e4;
  --text:#2b2b2b;
  --muted:#3a4754;
  --green:#3d8b2f;
  --dot:#3f9a3a;
  --white:#ffffff;
}
*{box-sizing:border-box;margin:0;padding:0}
html,body{width:1200px;height:960px;overflow:hidden}
body{position:relative;background:var(--page);font-family:"Open Sans",Arial,sans-serif;color:var(--text);font-size:16px}
.topbar{position:absolute;left:0;top:0;width:1200px;height:51px;background:var(--navy);color:var(--white)}
.brand{position:absolute;left:19px;top:11px;font-size:22px;font-weight:700;letter-spacing:.2px}
.nav-item{position:absolute;top:14px;font-size:17px;display:flex;align-items:center;gap:9px}
.nav-item svg{fill:var(--white)}
.status-select{position:absolute;left:644px;top:12px;width:144px;height:27px;background:var(--white);border-radius:3px;color:var(--text);font-size:16px;display:flex;align-items:center;padding-left:12px;gap:10px}
.status-select .dot{width:10px;height:10px;border-radius:50%;background:var(--dot)}
.status-select .arrows{position:absolute;right:10px;top:5px;font-size:9px;line-height:8px;color:#555}
.copyright{position:absolute;right:17px;top:14px;font-size:16px}

.panel{position:absolute;background:var(--panel);border:1px solid var(--line);border-radius:3px;overflow:hidden}
.visitors{left:11px;top:63px;width:1177px;height:422px;background:var(--grid-bg)}
.grid{border-collapse:collapse;width:100%;font-size:15px;table-layout:fixed}
.grid th{height:55px;background:linear-gradient(var(--head-top),var(--head-bottom));font-weight:400;text-align:left;padding-left:20px;border-right:1px solid var(--line);border-bottom:1px solid var(--line);color:var(--text)}
.grid th.center,.grid td.center{text-align:center;padding-left:0}
.grid td{height:49px;padding-left:20px;border-right:1px solid var(--white);border-bottom:1px solid var(--white);white-space:nowrap;overflow:hidden;text-overflow:ellipsis}
.grid td.ip{padding-left:19px}
.grid td.ip svg{vertical-align:-4px;margin-right:8px;fill:var(--muted)}
.chatting{color:var(--green)}
.plain-mark{display:inline-block;width:20px;height:20px;background:var(--muted);vertical-align:middle}
.plain-mark.round{border-radius:50%}

.chat-panel{left:12px;top:496px;width:912px;height:437px}
.tabs{height:61px;background:linear-gradient(var(--head-top),var(--head-bottom));border-bottom:1px solid var(--line);position:relative}
.tab{position:absolute;top:12px;height:50px;display:flex;align-items:center;gap:9px;font-size:17px;padding:0 14px}
.tab svg{fill:var(--muted)}
.tab.active{left:12px;width:159px;background:var(--white);border:1px solid var(--line);border-bottom:none;border-radius:3px 3px 0 0}
.push-row{position:absolute;top:82px;left:22px;display:flex;gap:6px}
.push{width:294px;height:42px;border:1px solid var(--line);border-radius:3px;background:linear-gradient(#f9f9f9,#ececec);display:flex;align-items:center;padding-left:14px;gap:9px;font-size:16px;position:relative}
.push svg{fill:var(--muted)}
.push .caret{position:absolute;right:12px;top:16px;width:0;height:0;border-left:7px solid transparent;border-right:7px solid transparent;border-top:10px solid var(--muted)}
.chat-title{position:absolute;left:24px;top:143px;font-size:19px;font-weight:700;color:var(--navy-text)}
.chat-title span{color:var(--green)}
.messages{position:absolute;left:24px;top:187px;font-size:15px;line-height:27px}
.messages b{font-weight:700;color:var(--navy-text)}
.messages b.visitor{color:var(--green)}
.composer{position:absolute;left:0;bottom:0;width:100%;height:47px;border-top:1px solid var(--line);display:flex;align-items:center;padding-left:24px;font-size:16px;color:#000}
.composer svg{position:absolute;right:24px;top:13px;fill:var(--muted)}

.operators{left:935px;top:496px;width:253px;height:437px}
.operators .head{height:61px;background:linear-gradient(var(--head-top),var(--head-bottom));border-bottom:1px solid var(--line);display:flex;align-items:center;padding-left:19px;gap:9px;font-size:17px}
.operators .head svg{fill:var(--muted)}
.operator{position:absolute;left:21px;top:84px;display:flex;align-items:center;gap:11px;font-size:16px}
.operator svg{fill:var(--muted)}
</style>
</head>
<body>
<header class="topbar">
  <div class="brand">Quorra Desk Talk</div>
  <div class="nav-item" style="left:327px"><svg width="18" height="15" viewBox="0 0 18 15"><path d="M0 2h6l2 2h8v2H4L1 14H0z M4 7h14l-3 8H1z"/></svg>File</div>
  <div class="nav-item" style="left:424px"><svg width="15" height="15" viewBox="0 0 15 15"><path d="M15 0L0 7l7 1 1 7z"/></svg>Actions</div>
  <div class="nav-item" style="left:551px"><svg width="22" height="13" viewBox="0 0 22 13"><rect x="0" y="0" width="22" height="13" rx="6.5"/><circle cx="6.5" cy="6.5" r="4.5" fill="#243447"/></svg>Status</div>
  <div class="status-select"><span class="dot"></span>Online<span class="arrows">▲<br>▼</span></div>
  <div class="copyright">Quorra Desk Talk © 2016</div>
</header>

<section class="panel visitors">
  <table class="grid">
    <colgroup><col style="width:185px"><col style="width:164px"><col style="width:108px"><col style="width:87px"><col style="width:467px"><col style="width:96px"><col></colgroup>
    <thead><tr><th>IP Address</th><th>Status</th><th class="center">Duration</th><th class="center">Pages</th><th>Location</th><th class="center">Browser</th><th class="center">OS</th></tr></thead>
    <tbody>
      <tr><td class="ip"><svg width="22" height="18" viewBox="0 0 22 18"><path d="M11 0C5 0 0 3.5 0 8c0 2.3 1.3 4.3 3.4 5.8L2 18l5-2.8c1.2.4 2.6.6 4 .6 6 0 11-3.5 11-8S17 0 11 0z"/></svg>10.214.63.72</td><td>Chatting <span class="chatting">“mrowenby”</span></td><td class="center">0:40:01</td><td class="center">17</td><td>https://www.brightlanehosting.com/billing/admin/supportti ...</td><td class="center"><span class="plain-mark round"></span></td><td class="center"><span class="plain-mark"></span></td></tr>
      <tr><td class="ip"><svg width="18" height="18" viewBox="0 0 18 18"><circle cx="9" cy="5" r="5"/><path d="M0 18c0-5 4-7 9-7s9 2 9 7z"/></svg>10.214.63.72</td><td>In Site</td><td class="center">0:40:01</td><td class="center">1</td><td>https://www.brightlanehosting.com/billing/admin/supportti ...</td><td class="center"><span class="plain-mark round"></span></td><td class="center"><span class="plain-mark round"></span></td></tr>
      <tr><td class="ip"><svg width="18" height="18" viewBox="0 0 18 18"><circle cx="9" cy="5" r="5"/><path d="M0 18c0-5 4-7 9-7s9 2 9 7z"/></svg>10.214.63.72</td><td>In Site</td><td class="center">0:40:01</td><td class="center">1</td><td>https://www.brightlanehosting.com/billing/admin/supportti ...</td><td class="center"><span class="plain-mark round"></span></td><td class="center"><span class="plain-mark round"></span></td></tr>
    </tbody>
  </table>
</section>

<section class="panel chat-panel">
  <div class="tabs">
    <div class="tab active"><svg width="17" height="17" viewBox="0 0 17 17"><circle cx="8.5" cy="8.5" r="8.5"/><rect x="7.3" y="7" width="2.4" height="6" fill="#fff"/><circle cx="8.5" cy="4.6" r="1.3" fill="#fff"/></svg>Visitors Info</div>
    <div class="tab" style="left:186px"><svg width="18" height="14" viewBox="0 0 18 14"><path d="M0 0h18v14H0z M2 2v2h14V2z M2 6v2h14V6z M2 10v2h14v-2z"/></svg>Footprints</div>
    <div class="tab" style="left:318px"><svg width="19" height="15" viewBox="0 0 19 15"><ellipse cx="8" cy="6" rx="8" ry="6"/><path d="M2 10l-1 5 5-3z"/></svg>Chat</div>
  </div>
  <div class="push-row">
    <div class="push"><svg width="15" height="15" viewBox="0 0 15 15"><path d="M7.5 0L13 6H9v5H6V6H2z M0 12h15v3H0z"/></svg>Push Responses<span class="caret"></span></div>
    <div class="push"><svg width="16" height="16" viewBox="0 0 16 16"><path d="M6 10l4-4M4.5 7.5l-2 2a2.5 2.5 0 003.5 3.5l2-2M11.5 8.5l2-2A2.5 2.5 0 0010 3l-2 2" stroke="#3a4754" stroke-width="2" fill="none"/></svg>Push Links<span class="caret"></span></div>
    <div class="push"><svg width="14" height="17" viewBox="0 0 14 17"><path d="M0 0h9l5 5v12H0z M2 2v13h10V6H8V2z M3 13l3-4 2 2 1-1 2 3z"/></svg>Push Images<span class="caret"></span></div>
  </div>
  <h2 class="chat-title">You are now chatting with <span>“mrowenby”</span></h2>
  <div class="messages">
    <p><b>Dana K.:</b> Hello mrowenb, how can I assist you today?</p>
    <p><b class="visitor">mrowenby.:</b> Hi I need some help.</p>
    <p><b>Dana K.:</b> Okay, how can I help?</p>
  </div>
  <div class="composer">Hello still the|<svg width="20" height="19" viewBox="0 0 20 19"><path d="M20 0L0 8l6 2 1 9 3-5 5 3z"/></svg></div>
</section>

<aside class="panel operators">
  <div class="head"><svg width="18" height="18" viewBox="0 0 18 18"><circle cx="9" cy="9" r="8" fill="none" stroke="#3a4754" stroke-width="2"/><circle cx="9" cy="9" r="4" fill="none" stroke="#3a4754" stroke-width="2"/><path d="M3 3l3 3M15 3l-3 3M3 15l3-3M15 15l-3-3" stroke="#3a4754" stroke-width="2"/></svg>Operators</div>
  <div class="operator"><svg width="18" height="18" viewBox="0 0 18 18"><circle cx="9" cy="5" r="5"/><path d="M0 18c0-5 4-7 9-7s9 2 9 7z"/></svg>Dana K</div>
</aside>
</body>
</html>
```